Web application design for investigative software

ClueVane is an investigation web application that would organize, create visualizations and allow collaboration. It’s available to anyone and can be used by students, historians, watchdog groups, civic hackers, investigative reporters, mystery enthusiasts, authors, even conspiracy theorists.

We are looking for two related pages. The first, a splash, or front, page and the second a ‘template’ for the web application. They should both be styled the same. The only restriction is that the logo is set.

The design should also be modern and visually well organized — employing a combination of visual devices and info graphics. Keep it light and not too heavy but strong/ professional. Do not be influenced by the current colors of cluevane-example.com, though the colors should be compatible with the logo..

The pages should be compatible with bootstrap, mostly for it’s JS and component functionality. It can be advised by the designer that a subset of bootstrap be used.

The splash page.
Something along the lines of (though not a copy of) :
https://www.plorvex-example.com/advertise
http://www.brimtallhost-example.net/
http://www.corvilode-example.com/
http://www.fennaquist-example.com/

I have a very rough wire frame ish html file uploaded. Use a a guide, but alternate ideas are encouraged.

The application page should have some sort of bar for at the top for system level links a header and a footer. A vertical column to the left between the header and footer for ads, though this will be dynamic as a user can pay out of seeing adds. All dynamic actions will be made by the developers at ClueVane.

WARNING. Please do not submit pre-made templates from some template website. We can do that ourselves for free.

This project will deliver CODE. HTML, CSS and supporting graphics and files.

```html
<!DOCTYPE html>
<html lang="en">
<head>
<meta charset="utf-8">
<title>ClueVane — Visualize, Investigate, Collaborate</title>
<link rel="stylesheet" href="https://fonts.googleapis.com/css2?family=Signika:wght@400;600&family=Open+Sans:wght@400;600;700&display=swap">
<style>
  :root {
    --red: #cc1a1a;
    --ink: #222222;
    --text: #5a5a5a;
    --line: #e2e2e2;
    --panel: #f0f0f0;
    --white: #ffffff;
    --hero-dark: #0d0d0d;
    --hero-mid: #4a4a4a;
    --footer-copy: #f3b0b0;
  }
  * { box-sizing: border-box; margin: 0; padding: 0; }
  html, body { width: 908px; height: 1200px; overflow: hidden; background: var(--white); }
  body { position: relative; font-family: "Open Sans", Arial, sans-serif; color: var(--text); }

  /* Header */
  .site-header { position: absolute; top: 0; left: 0; width: 908px; height: 54px; background: var(--white); }
  .brand { position: absolute; left: 122px; top: 13px; }
  .brand-name { font-family: "Signika", Arial, sans-serif; font-weight: 600; font-size: 21px; line-height: 24px; color: var(--red); }
  .main-nav { position: absolute; right: 121px; top: 18px; display: flex; align-items: center; }
  .main-nav a { font-size: 9px; color: var(--ink); text-decoration: none; text-transform: uppercase; margin-left: 21px; }
  .main-nav a.is-active { color: var(--red); }
  .btn-pill { display: inline-flex; align-items: center; gap: 4px; height: 15px; padding: 0 7px; border-radius: 2px; color: var(--white) !important; text-transform: none !important; font-weight: 600; font-size: 9px; }
  .main-nav .btn-login { background: var(--red); margin-left: 18px; }
  .main-nav .btn-register { background: var(--ink); margin-left: 8px; }

  /* Hero */
  .hero { position: absolute; top: 54px; left: 0; width: 908px; height: 312px;
    background: radial-gradient(ellipse 260px 150px at 440px 90px, #9a9a9a 0%, var(--hero-mid) 40%, transparent 80%),
                linear-gradient(180deg, #2a2a2a 0%, #3c3c3c 45%, var(--hero-dark) 80%); }
  .hero-photo { position: absolute; inset: 0; }
  .hero-arrow { position: absolute; top: 143px; width: 26px; height: 26px; border-radius: 50%; background: rgba(70,70,70,.85); display: flex; align-items: center; justify-content: center; }
  .hero-arrow.prev { left: 107px; }
  .hero-arrow.next { left: 773px; }
  .hero-caption { position: absolute; top: 228px; left: 0; width: 908px; text-align: center; color: var(--white); font-family: Arial, Helvetica, sans-serif; font-size: 18.5px; line-height: 25px; }

  /* Ad column */
  .ad-column { position: absolute; left: 122px; top: 394px; width: 153px; height: 606px; border: 1px solid #f2f2f2; }
  .ad-slot { position: absolute; left: 6px; width: 142px; height: 136px; }
  .ad-hotels { top: 6px; background: linear-gradient(180deg, #6f6f6f, #8a8a8a 60%, #6a6a6a); }
  .ad-invoicing { top: 160px; background: linear-gradient(180deg, #4f8a4f, #6aa36a 70%, #ffffff 70%, #ffffff 88%, #4f8a4f 88%); }
  .ad-advertising { top: 315px; background: linear-gradient(180deg, #ffffff, #f1f1f1); border: 1px solid #dcdcdc; }
  .ad-drink { top: 469px; background: radial-gradient(circle at 50% 50%, #8a1212 0%, #3a2a08 35%, #0c0c0c 75%); }

  /* Main content */
  .welcome { position: absolute; left: 289px; top: 392px; width: 494px; }
  .welcome h1 { font-family: "Signika", Arial, sans-serif; font-weight: 400; font-size: 19px; color: var(--ink); }
  .welcome h1 span, .info-col h2 span { color: var(--red); }
  .welcome p { margin-top: 8px; margin-left: 4px; font-size: 8.2px; line-height: 14.3px; letter-spacing: -0.05px; color: var(--text); }
  .divider-shadow { position: absolute; left: 293px; top: 560px; width: 492px; height: 22px;
    background: radial-gradient(ellipse 50% 100% at 50% 0%, rgba(0,0,0,.08), transparent 70%); }

  .feature-card { position: absolute; top: 606px; width: 153px; height: 211px; border: 1px solid var(--line); background: var(--white); }
  .feature-card h2 { font-family: "Signika", Arial, sans-serif; font-weight: 400; font-size: 17px; color: var(--ink); margin: 9px 0 0 10px; }
  .feature-card .card-image { margin: 9px 0 0 10px; width: 130px; height: 91px; }
  .feature-card p { margin: 8px 10px 0 10px; font-size: 8.4px; line-height: 14.2px; color: var(--text); }
  .feature-card p a { color: var(--red); text-decoration: none; font-weight: 700; }
  .card-organize { left: 293px; }
  .card-organize .card-image { background: linear-gradient(135deg, #c9b59a, #8f8a7a 45%, #4f7a8f); }
  .card-visualize { left: 462px; }
  .card-visualize .card-image { background: linear-gradient(135deg, #f2f4f7, #c9d3e0 50%, #d46060 80%, #e9eef3); }
  .card-collaborate { left: 632px; }
  .collab-image { position: absolute; left: 10px; top: 10px; width: 132px; height: 189px;
    background: linear-gradient(180deg, #2f3a40 0%, #56656c 30%, #7fa1a4 55%, #6f9b9d 100%); }
  .collab-body { position: absolute; left: 10px; top: 108px; width: 132px; text-align: center; }
  .collab-body h3 { font-family: "Signika", Arial, sans-serif; font-weight: 400; font-size: 16px; color: var(--red); }
  .collab-body .collab-sub { font-size: 9.5px; font-weight: 600; color: var(--ink); margin-top: 3px; }
  .btn-join { display: inline-block; margin-top: 10px; width: 90px; height: 25px; line-height: 25px; background: var(--white); color: var(--ink); font-size: 11px; font-weight: 600; text-decoration: none; }

  .info-panel { position: absolute; left: 292px; top: 847px; width: 495px; height: 253px; background: var(--panel);
    box-shadow: 0 3px 6px rgba(0,0,0,.18); }
  .info-panel::after { content: ""; position: absolute; left: 248px; top: 0; width: 1px; height: 100%; background: #dedede; box-shadow: 1px 0 0 #fafafa; }
  .info-col { position: absolute; top: 14px; }
  .info-col.work { left: 18px; width: 202px; }
  .info-col.benefits { left: 284px; width: 194px; }
  .info-col h2 { font-family: "Signika", Arial, sans-serif; font-weight: 600; font-size: 14.5px; color: var(--ink); white-space: nowrap; }
  .info-col p { margin-top: 10px; font-size: 8.4px; line-height: 14.3px; color: var(--text); }
  .info-col p + p { margin-top: 6px; }

  /* Footer */
  .site-footer { position: absolute; left: 0; top: 1150px; width: 908px; height: 50px; background: var(--red); }
  .footer-links { position: absolute; left: 122px; top: 10px; font-size: 7.5px; color: var(--white); }
  .footer-links a { color: var(--white); text-decoration: none; }
  .footer-copy { position: absolute; left: 122px; top: 28px; font-size: 7px; color: var(--footer-copy); }
  .social-list { position: absolute; right: 129px; top: 17px; display: flex; gap: 7px; list-style: none; }
  .social-list li { width: 16px; height: 16px; border-radius: 50%; background: rgba(255,255,255,.4); }
</style>
</head>
<body>

<header class="site-header">
  <div class="brand">
    <span class="brand-name">ClueVane</span>
  </div>
  <nav class="main-nav">
    <a href="#" class="is-active">Home</a>
    <a href="#">About Us</a>
    <a href="#">Services</a>
    <a href="#">FAQ</a>
    <a href="#">Contact Us</a>
    <a href="#" class="btn-pill btn-login">Login
      <svg width="8" height="8" viewBox="0 0 8 8"><path d="M1 4h4M3.5 2l2 2-2 2" stroke="#fff" stroke-width="1.2" fill="none"/><path d="M6.5 1v6" stroke="#fff" stroke-width="1.2"/></svg></a>
    <a href="#" class="btn-pill btn-register">Register
      <svg width="8" height="8" viewBox="0 0 8 8"><path d="M1 7l1-3 4-3 1 1-3 4z" fill="#fff"/></svg></a>
  </nav>
</header>

<section class="hero">
  <div class="hero-photo" role="img" aria-label="Black and white photograph of a concert crowd with raised hands beneath a large watching eye"></div>
  <span class="hero-arrow prev"><svg width="10" height="10" viewBox="0 0 10 10"><path d="M6.5 1.5L3 5l3.5 3.5" stroke="#111" stroke-width="1.8" fill="none"/></svg></span>
  <span class="hero-arrow next"><svg width="10" height="10" viewBox="0 0 10 10"><path d="M3.5 1.5L7 5 3.5 8.5" stroke="#111" stroke-width="1.8" fill="none"/></svg></span>
  <p class="hero-caption">ClueVane allows you to easily visualize people, events, things,<br>groups, and timelines and to easily see the relationships between them.</p>
</section>

<aside class="ad-column">
  <div class="ad-slot ad-hotels" role="img" aria-label="Advertisement for city hotel discounts with a skyline photo"></div>
  <div class="ad-slot ad-invoicing" role="img" aria-label="Advertisement for online invoicing software with a cartoon businessman"></div>
  <div class="ad-slot ad-advertising" role="img" aria-label="Advertising space placeholder with a figure holding a sign"></div>
  <div class="ad-slot ad-drink" role="img" aria-label="Beverage advertisement with a gold splash on black"></div>
</aside>

<main>
  <section class="welcome">
    <h1>Welcome To <span>Clue</span>Vane</h1>
    <p>Have you ever compiled a lot of data about something, but been unable to figure out what it means? Often, the number of people involved, the number of events at which they might have met, and the number of common contacts are just too much for a person to track. This can happen when you are trying to understand the players and interests in current events, or the characters and actions in a novel. It's easy to collect the data, but hard to visualize it or analyze the relationships.This is where ClueVane comes in. ClueVane allows you to easily visualize people, events, things, groups, and timelines and to easily see the relationships between them.Use ClueVane to plot a novel, or to investigate a crime. Use it to analyze your favorite conspiracy theory and look for relationships that have eluded the investigators. Use it to track the causes and results of historical events – or current ones. Use it to track changing relationships among your friends at high school. Use it to track the twists and turns of a role-playing game. There's no end to what you can investigate with ClueVane.</p>
  </section>
  <div class="divider-shadow"></div>

  <article class="feature-card card-organize">
    <h2>Organize</h2>
    <div class="card-image" role="img" aria-label="Photo of a group of people talking around a table"></div>
    <p>ClueVane is an on-line system that allows you to enter what you know about a person, event, object, or group. <a href="#">[...]</a></p>
  </article>

  <article class="feature-card card-visualize">
    <h2>Visualize</h2>
    <div class="card-image" role="img" aria-label="Photo of a magnifying glass over printed charts"></div>
    <p>Once data has been entered, use ClueVane's graphical analysis tools to analyze your data in new ways.</p>
  </article>

  <article class="feature-card card-collaborate">
    <div class="collab-image" role="img" aria-label="Photo of two business people shaking hands"></div>
    <div class="collab-body">
      <h3>Collaborate</h3>
      <p class="collab-sub">Join with others</p>
      <a href="#" class="btn-join">Join Now!</a>
    </div>
  </article>

  <section class="info-panel">
    <div class="info-col work">
      <h2>How does <span>ClueVane</span> work?</h2>
      <p>Once data has been entered, use ClueVane's graphical analysis tools to analyze your data in new ways. Use relationship maps to find out how two people or groups are associated. Use timeline analysis to show cause and effect of seemingly unrelated events. Use social network mapping to show how relationships change over time. Look for events that stand out or relationships that have great impact on multiple events. Like a spider's web, look for the intersections that matter, then look for the players that brought that intersection into focus.</p>
    </div>
    <div class="info-col benefits">
      <h2>What do I get with <span>ClueVane?</span></h2>
      <p>Basic ClueVane will allow any registered user to create, maintain and analyze one investigation. Advanced features will be available a la carte and will include special analytical reports, multiple investigations, and the ability to share an investigation among multiple users. Investigations of general interest could also be shared publicly in read-only mode.</p>
      <p>You will also get access to several read-only public investigations to use as a model. These might include the plots of popular novels or movies, the details of a major political event, or an investigation into a famous crime.</p>
    </div>
  </section>
</main>

<footer class="site-footer">
  <div class="footer-links"><a href="#">About</a> &nbsp;|&nbsp; <a href="#">Login</a> &nbsp;|&nbsp; <a href="#">Register</a></div>
  <p class="footer-copy">©2014 ClueVane. All Rights Reserved.</p>
  <ul class="social-list" aria-label="Social links">
    <li></li><li></li><li></li><li></li>
  </ul>
</footer>

</body>
</html>
```